vQ CARELINE (Brochure Design)

i need a proffesional brochure made. we are a mobile medical service company providing mobile Arterial Blood Gases(ABG's). Respiratory & Ventilator Consultation services. Ventilator and Tracheostomy training courses. and mobile vaccine administration.

this is my first time making a brochure so any and all advice/guidance will be appreciated.

i am thinking prints will be 8.5 inches x 11 inches (TRI-FOLD and BI-FOLD)

i have uploaded my business card design and logo design for reference.
as this brochure project continues ill update needs of the project descriptions.

Introduction: At vq CARELINE, we're dedicated to enhancing healthcare services by providing exceptional mobile arterial blood gases, respiratory and ventilator consultation services. Our core values revolve around excellence, compassion and accessibility. We believe that every individual deserves the highest standard of care, and we're committed to delivering that through expert guidance and top-notch training courses. Your health is at the heart of what we do, and we're here to support you on your journey to better respiratory health.

Mobile Arterial Blood Gases : Our mobile Arterial Blood Gas service offers quick, on-the-spot analysis of pH, oxygen, and carbon dioxide levels in your the blood. This service enables rapid adjustments to treatment plans for more effective respiratory care.

Ventilator and Tracheostomy Training: Our ventilator and tracheostomy course empowers caregivers and healthcare professionals to manage ventilators and care for tracheostomy patients with expertise. This training enhances patient safety, treatment outcomes, and healthcare provider confidence. vQ Careline your choice for top-notch care, convenience, and peace of mind.

Respiratory Consulting: Our respiratory consulting services provide expert guidance and support for individuals with respiratory / ventilator concerns. Benefits include personalized treatment plans, better management of respiratory conditions, and improved overall lung health. vQ Careline is your trusted partner for a breath of fresh air.

Target Market(s)

Sub-Acute facilities, Pulmonary Clinics, Pulmonologists, Nurses, Caregivers, Hospice and homehealth companies.

Industry/Entity Type

Medical; Respiratory; Nursing

Requirements
Must have
• proffesional simple design.

```html
<!DOCTYPE html>
<html lang="en">
<head>
<meta charset="utf-8">
<title>vQ CARELINE – Tri-fold Brochure</title>
<link href="https://fonts.googleapis.com/css2?family=Montserrat:wght@400;500;600;700&family=Roboto+Condensed:wght@400;700&display=swap" rel="stylesheet">
<style>
  :root{
    --blue:#0b5cb5;
    --blue-deep:#0a3f8f;
    --blue-bright:#1670d0;
    --green:#1f9e3e;
    --green-teal:#149068;
    --ink:#2a2a2a;
    --paper:#f4f6f8;
    --backdrop:#e9ebee;
  }
  *{box-sizing:border-box;margin:0;padding:0}
  html,body{width:1137px;height:1200px;overflow:hidden;background:var(--backdrop)}
  body{font-family:"Montserrat",sans-serif;color:var(--ink);position:relative}

  .spread{position:absolute;left:163px;width:810px;height:588px;display:flex;box-shadow:0 4px 14px rgba(0,0,0,.18)}
  .spread--outside{top:8px}
  .spread--inside{top:604px}
  .panel{position:relative;width:270px;height:588px;overflow:hidden}

  .photo{position:absolute}

  /* brand */
  .brand{position:absolute;display:flex;align-items:center;gap:8px;font-weight:500;letter-spacing:.2px}
  .brand__mark{width:22px;height:22px;background:currentColor;flex:none}

  /* outside: consulting */
  .panel--consulting{background:var(--paper)}
  .panel--consulting .photo{left:0;top:0;width:270px;height:184px;background:linear-gradient(135deg,#8a7d8e,#5b4f6a 45%,#c9c9cf)}
  .abg-card{position:absolute;left:22px;top:152px;width:248px;height:254px;background:#fff;border-top:2px solid var(--blue)}
  .abg-card__title{font-family:"Roboto Condensed",sans-serif;font-weight:700;font-size:11px;text-align:center;margin-top:12px;color:#222}
  .abg-table{position:absolute;left:16px;top:44px;width:118px;border-collapse:collapse;font-family:"Roboto Condensed",sans-serif;font-size:8.5px;color:#111}
  .abg-table th,.abg-table td{border:1px solid #333;padding:3px 3px;text-align:center;line-height:1.15}
  .abg-card .photo{left:140px;top:46px;width:88px;height:196px;background:linear-gradient(160deg,#f3d3c8,#e59a8a 55%,#f6e2dc)}
  .section-title{position:absolute;font-weight:700;text-transform:uppercase;color:var(--blue)}
  .panel--consulting .section-title{left:22px;top:424px;font-size:12.5px}
  .body-copy{position:absolute;font-size:10.6px;line-height:14.8px}
  .panel--consulting .body-copy{left:22px;top:448px;width:234px;color:#333}

  /* outside: contact */
  .panel--contact{background:linear-gradient(20deg,#0b56b0 0%,#137f80 45%,#1fa348 100%);color:#fff}
  .panel--contact .brand{left:46px;top:250px;font-size:20px;color:#fff}
  .contact-rule{position:absolute;left:136px;top:294px;width:134px;height:1px;background:rgba(255,255,255,.5)}
  .contact-list{position:absolute;left:0;top:304px;width:270px;list-style:none;text-align:center}
  .contact-list li{height:55px;font-size:13.4px;letter-spacing:.5px}
  .contact-list svg{display:block;margin:0 auto 6px;width:12px;height:12px;fill:#fff}
  .contact-rule--low{top:534px;left:0;width:270px;background:rgba(255,255,255,.25)}

  /* outside: cover */
  .panel--cover{background:linear-gradient(180deg,#fff,var(--paper))}
  .panel--cover .brand{left:26px;top:52px;font-size:23px;color:var(--green)}
  .panel--cover .brand__mark{background:var(--blue);width:28px;height:28px}
  .panel--cover .photo{left:0;top:87px;width:270px;height:287px;background:linear-gradient(150deg,#d9d9d9,#9b9b9b 50%,#e6e6e6);clip-path:polygon(28% 0,100% 0,100% 100%,0 100%,0 26%)}
  .cover-title{position:absolute;right:10px;top:360px;text-align:right;font-weight:700;font-size:20px;line-height:27px}
  .cover-title span{display:block}
  .cover-title .l1{color:var(--blue)}
  .cover-title .l2{color:var(--green)}
  .cover-services{position:absolute;left:15px;top:432px;width:238px;height:54px;border:1.5px solid var(--green);border-left:none;padding:10px 10px 0 4px;font-size:10.6px;font-weight:700;line-height:14.2px;color:var(--blue)}
  .cover-url{position:absolute;left:0;width:270px;top:540px;text-align:center;font-weight:700;font-size:12.5px;color:var(--green)}

  /* inside: introduction */
  .panel--intro{background:#f7f8fa}
  .panel--intro .section-title{left:17px;top:42px;font-size:15px}
  .panel--intro .body-copy{left:17px;top:74px;width:242px;font-size:11.2px;line-height:16.2px;color:#222}
  .panel--intro .photo{left:27px;top:305px;width:236px;height:150px;background:linear-gradient(180deg,#dfe6f2,#8fa8d4 60%,#eef2f8)}
  .intro-band{position:absolute;left:0;top:0}
  .feature-list{position:absolute;left:0;top:520px;width:270px;display:flex;list-style:none;color:#fff}
  .feature-list li{flex:1;text-align:center;font-size:10.6px;line-height:12px}
  .feature-list svg{display:block;margin:0 auto 6px;width:30px;height:30px}

  /* inside: ABG */
  .panel--abg{background:linear-gradient(180deg,#1564c4 0%,#0f6aa8 35%,#13866a 70%,#0f6d4f 100%);color:#fff}
  .panel--abg .section-title{left:22px;top:40px;font-size:14.5px;line-height:19px;color:#fff}
  .panel--abg .body-copy{left:22px;top:96px;width:236px;font-size:10.8px;line-height:16.2px}
  .panel--abg .photo--device{left:70px;top:226px;width:142px;height:145px;background:linear-gradient(160deg,#b9c8e6,#6d86bd 60%,#d4dbe6)}
  .panel--abg .photo--procedure{left:27px;top:428px;width:229px;height:120px;background:linear-gradient(135deg,#e8d2c2,#7f9fd8 55%,#3c63c4)}

  /* inside: training */
  .panel--training{background:var(--blue-bright)}
  .panel--training .photo--syringe{left:0;top:0;width:270px;height:252px;background:linear-gradient(135deg,#e8e6ea,#c9b4b0 50%,#8c2a2a);clip-path:polygon(0 0,100% 0,100% 18%,0 100%)}
  .panel--training .photo--vent{left:128px;top:158px;width:138px;height:174px;background:linear-gradient(180deg,#4a3f8f 0 10%,#eceef2 10% 86%,#4a3f8f 86%)}
  .panel--training .section-title{left:18px;top:356px;font-size:13px;line-height:17px;color:#fff}
  .panel--training .body-copy{left:18px;top:402px;width:244px;font-size:10.4px;line-height:13.3px;color:#fff}
  .panel--training .body-copy p+p{margin-top:13px}
</style>
</head>
<body>

<!-- Outside of the tri-fold -->
<section class="spread spread--outside">

  <article class="panel panel--consulting">
    <div class="photo" role="img" aria-label="Photo of a nurse adjusting a ventilator beside a resting patient"></div>
    <div class="abg-card">
      <p class="abg-card__title">Arterial Blood Gas (ABG)</p>
      <table class="abg-table">
        <tr><th>ABG</th><th>Normal range</th></tr>
        <tr><td>O<sub>2</sub>CT</td><td>15-23% per<br>100 mL of blood</td></tr>
        <tr><td>pH</td><td>7.35-7.45</td></tr>
        <tr><td>PaCO<sub>2</sub></td><td>35-45 mmHg</td></tr>
        <tr><td>PaO<sub>2</sub></td><td>80-100 mmHg</td></tr>
        <tr><td>HCO<sub>3</sub></td><td>22-26 mEq/L</td></tr>
        <tr><td>O<sub>2</sub>Sat</td><td>95-100%</td></tr>
      </table>
      <div class="photo" role="img" aria-label="Illustration of a forearm and hand showing the artery used for blood sampling"></div>
    </div>
    <h2 class="section-title">Respiratory Consulting:</h2>
    <p class="body-copy">Our respiratory consulting services provide expert guidance and support for individuals with respiratory / ventilator concerns. Benefits include personalized treatment plans, better management of respiratory conditions, and improved overall lung health. vQ Careline is your trusted partner for a breath of fresh air.</p>
  </article>

  <article class="panel panel--contact">
    <div class="brand"><span class="brand__mark"></span>vQ CARELINE</div>
    <div class="contact-rule"></div>
    <ul class="contact-list">
      <li><svg viewBox="0 0 24 24"><path d="M6.6 10.8a15 15 0 0 0 6.6 6.6l2.2-2.2c.3-.3.7-.4 1-.2 1.1.4 2.3.6 3.6.6.6 0 1 .4 1 1V20c0 .6-.4 1-1 1A17 17 0 0 1 3 4c0-.6.4-1 1-1h3.5c.6 0 1 .4 1 1 0 1.3.2 2.5.6 3.6.1.3 0 .7-.2 1z"/></svg>555.014.2994</li>
      <li><svg viewBox="0 0 24 24"><path d="M2 5h20v2l-10 6L2 7zM2 9l10 6 10-6v10H2z"/></svg>info@vqcarelinegroup.com</li>
      <li><svg viewBox="0 0 24 24"><path d="M6 2h9l3 3v5H6zM3 11h18v10H3zm3 3v2h12v-2z"/></svg>555.019.2223</li>
      <li><svg viewBox="0 0 24 24" fill="none" stroke="#fff" stroke-width="2" style="fill:none"><circle cx="12" cy="12" r="9"/><path d="M3 12h18M12 3c3 3 3 15 0 18M12 3c-3 3-3 15 0 18"/></svg>vqcarelinegroup.com</li>
    </ul>
    <div class="contact-rule contact-rule--low"></div>
  </article>

  <article class="panel panel--cover">
    <div class="brand"><span class="brand__mark"></span>vQ CARELINE</div>
    <div class="photo" role="img" aria-label="Black and white photo of a patient resting in a hospital bed with a ventilator"></div>
    <h1 class="cover-title"><span class="l1">MOBILE ARTERIAL</span><span class="l2">BLOOD GASES(ABG'S).</span></h1>
    <p class="cover-services">Respiratory &amp; Ventilator Consultation services. Ventilator and Tracheostomy training courses and mobile vaccine administration.</p>
    <p class="cover-url">www.vqcarelinegroup.com</p>
  </article>
</section>

<!-- Inside of the tri-fold -->
<section class="spread spread--inside">

  <article class="panel panel--intro">
    <svg class="intro-band" width="270" height="588" viewBox="0 0 270 588">
      <polygon points="0,346 205,480 270,428 270,588 0,588" fill="var(--blue-deep)"/>
      <polygon points="205,480 270,428 270,588 120,588" fill="#0c4fa6"/>
    </svg>
    <h2 class="section-title">Introduction:</h2>
    <p class="body-copy">At vQ CARELINE, we're dedicated to enhancing healthcare services by providing exceptional mobile arterial blood gases, respiratory and ventilator consultation services. Our core values revolve around excellence, compassion and accessibility. We believe that every individual deserves the highest standard of care, and we're committed to delivering that through expert guidance and top-notch training courses. Your health is at the heart of what we do, and we're here to support you on your journey to better respiratory health.</p>
    <div class="photo" role="img" aria-label="Photo of two portable ventilator units"></div>
    <ul class="feature-list">
      <li><svg viewBox="0 0 30 30" fill="none" stroke="#fff" stroke-width="1.4"><circle cx="15" cy="15" r="14"/><path d="M15 8v8M15 12l-3 2M15 12l3 2" /><path d="M12 11c-3 1-5 6-4 9 1 2 4 1 4-1zM18 11c3 1 5 6 4 9-1 2-4 1-4-1z" fill="#fff"/></svg>Respiratory<br>Consultations</li>
      <li><svg viewBox="0 0 30 30" fill="none" stroke="#fff" stroke-width="1.4"><circle cx="15" cy="15" r="14"/><path d="M9 21l9-9M16 10l4 4M19 9l2 2M9 21l-2 2"/><path d="M10 18l3-3 2 2-3 3z" fill="#fff"/></svg>In-house<br>ABG’s</li>
      <li><svg viewBox="0 0 30 30" fill="none" stroke="#fff" stroke-width="1.4"><circle cx="15" cy="15" r="14"/><rect x="9" y="8" width="12" height="10" rx="1"/><path d="M11 13h3l1-2 1 4 1-2h2M13 18v4h4v-4"/></svg>Ventilator<br>Training</li>
    </ul>
  </article>

  <article class="panel panel--abg">
    <h2 class="section-title">Mobile Arterial Blood<br>Gases :</h2>
    <p class="body-copy">Our mobile Arterial Blood Gas service offers quick, on-the-spot analysis of pH, oxygen, and carbon dioxide levels in your the blood. This service enables rapid adjustments to treatment plans for more effective respiratory care.</p>
    <div class="photo photo--device" role="img" aria-label="Photo of a portable ventilator"></div>
    <div class="photo photo--procedure" role="img" aria-label="Photo of gloved hands drawing an arterial blood sample from a wrist"></div>
  </article>

  <article class="panel panel--training">
    <div class="photo photo--syringe" role="img" aria-label="Photo of a blood sample being drawn into a syringe"></div>
    <div class="photo photo--vent" role="img" aria-label="Photo of a transport ventilator unit"></div>
    <h2 class="section-title">Ventilator and<br>Tracheostomy Training:</h2>
    <div class="body-copy">
      <p>Our ventilator and tracheostomy course empowers caregivers and healthcare professionals to manage ventilators and care for tracheostomy patients with expertise.</p>
      <p>This training enhances patient safety, treatment outcomes, and healthcare provider confidence. vQ Careline your choice for top-notch care, convenience, and peace of mind.</p>
    </div>
  </article>
</section>

</body>
</html>
```